Meridel Bidding Group Website

We are an food equipment auction company and are in need of an updated website. Old website found here: http://meridelbiddinggroup.example/ . We need to be able to share upcoming auctions, past auctions, companies we've worked with, needs to be mobile friendly. We will also need an easy to access back office where we can add new info, auction info, etc.

Target Market(s)

Equipment auctions, large food manufacturers, equipment resalers

Industry/Entity Type

Auction

Coding

Number of Pages Required

5+ page

Font styles to use
Sans Serif

Colors
acd136
ffffff

Requirements
Must have
• Back office where we can add new auctions
-mobile friendly
-contact us page,
-services page
-social media widgets
-must match our current logo
-current auctions on front page
- join mailing list
- past auctions / current auctions pages
Nice to have
• Would like it to be clean design, easy to view and find options, modern

```html
<!DOCTYPE html>
<html lang="en">
<head>
<meta charset="utf-8">
<title>Meridel Bidding Group</title>
<link href="https://fonts.googleapis.com/css2?family=Barlow:ital,wght@0,400;0,500;0,600;1,400&family=Barlow+Semi+Condensed:wght@400;500;600&display=swap" rel="stylesheet">
<style>
:root{
  --lime:#acd136;
  --lime-dark:#8fb12a;
  --slate:#3a4352;
  --slate-deep:#2f3744;
  --ink:#2b2f36;
  --text:#4a4f57;
  --white:#ffffff;
  --muted:#c9ced6;
}
*{box-sizing:border-box;margin:0;padding:0}
html,body{width:1200px;height:3315px;overflow:hidden;background:var(--white)}
body{position:relative;font-family:"Barlow",sans-serif;color:var(--text)}
.abs{position:absolute}
.cond{font-family:"Barlow Semi Condensed",sans-serif}
.hl{color:var(--lime)}
.pill{position:absolute;border:1.5px solid var(--lime);border-radius:20px;color:var(--lime-dark);font:600 12px "Barlow",sans-serif;letter-spacing:.6px;display:flex;align-items:center;justify-content:center;text-transform:uppercase}
.pill.solid{background:var(--lime);color:var(--white)}

/* header */
.brand{left:60px;top:32px;display:flex;align-items:center;gap:12px}
.brand-dot{width:34px;height:34px;background:var(--lime);border-radius:50%}
.brand-name{font:600 22px "Barlow Semi Condensed",sans-serif;color:var(--lime-dark);line-height:1}
.call{left:766px;top:23px;font:500 19px "Barlow Semi Condensed",sans-serif;color:var(--ink)}
.call span{color:var(--lime-dark)}
.nav{left:297px;top:80px;width:903px;height:40px;background:var(--slate)}
.nav a{position:absolute;top:0;height:40px;line-height:40px;color:var(--white);font:500 13px "Barlow",sans-serif;letter-spacing:.5px;text-decoration:none}
.nav .on{background:var(--lime)}

/* hero */
.hero{left:0;top:120px;width:1200px;height:530px;background:linear-gradient(180deg,#3d4654 0%,#5a616b 45%,#3e4652 100%)}
.hero-title{left:0;top:312px;width:1200px;text-align:center;font:400 40px/46px "Barlow Semi Condensed",sans-serif;color:var(--white);letter-spacing:1px}
.hero-title b{font-weight:500;color:var(--lime)}

/* welcome */
.sec-title{width:1200px;left:0;text-align:center;font:500 28px/34px "Barlow Semi Condensed",sans-serif;color:var(--ink)}
.welcome-media{left:207px;top:828px;width:321px;height:260px;background:linear-gradient(135deg,#8fb12a,#4a525e 60%,#a9b2bc)}
.welcome-copy{left:544px;top:818px;width:450px;font-size:11.5px;line-height:19.3px;color:var(--text)}
.welcome-copy p+p{margin-top:19px}

/* services */
.services{left:0;top:1174px;width:1200px;height:530px;background:var(--slate)}
.svc-title{left:208px;top:1248px;font:500 28px "Barlow Semi Condensed",sans-serif;color:var(--white)}
.svc-intro{left:208px;top:1298px;width:440px;font:400 14px/19px "Barlow Semi Condensed",sans-serif;color:var(--white);text-transform:uppercase}
.svc-item{position:absolute;display:flex;align-items:center;gap:10px;font:400 17px "Barlow Semi Condensed",sans-serif;color:var(--white)}
.svc-media{left:672px;top:1248px;width:320px;height:260px;background:linear-gradient(135deg,#8fb12a 0%,#5b6470 50%,#7a838d 100%);opacity:.85}

/* auctions */
.card{position:absolute;top:1843px;width:320px}
.card-img{width:320px;height:200px}
.card-date{margin-top:22px;font:500 12px "Barlow",sans-serif;color:var(--lime-dark)}
.card-title{margin-top:9px;font:400 17px/23px "Barlow",sans-serif;color:var(--ink)}
.card-loc{margin-top:6px;font:500 12px "Barlow",sans-serif;color:var(--lime-dark)}
.card .pill{position:relative;margin-top:26px;width:129px;height:31px}

/* testimonials */
.clients{left:0;top:2290px;width:1200px;height:433px;background:var(--slate)}
.quote{left:250px;top:2450px;width:700px;text-align:center;font:italic 400 17px/29px "Barlow",sans-serif;color:var(--white)}
.avatar{left:568px;top:2535px;width:64px;height:64px;border-radius:50%;background:radial-gradient(circle,#b9a089,#6d5a4c);border:2px solid var(--white)}
.person{left:0;top:2610px;width:1200px;text-align:center;color:var(--white);font-size:12.5px;line-height:19px}
.person b{font-weight:600;letter-spacing:.5px}

/* newsletter */
.newsletter{left:0;top:2723px;width:1200px;height:120px;background:var(--lime)}
.nl-title{left:88px;top:2754px;font:600 27px "Barlow Semi Condensed",sans-serif;color:var(--ink)}
.nl-sub{left:88px;top:2792px;font-size:12px;color:var(--ink)}
.nl-form{left:720px;top:2751px;width:391px;height:64px;background:var(--white);border-radius:32px}
.nl-btn{right:16px;top:15px;width:96px;height:36px;border-radius:18px;background:var(--slate);color:var(--white);font:600 12px "Barlow",sans-serif;display:flex;align-items:center;justify-content:center;letter-spacing:.5px}

/* footer */
.footer{left:0;top:2843px;width:1200px;height:472px;background:var(--slate)}
.ft-h{font:500 18px "Barlow Semi Condensed",sans-serif;color:var(--white)}
.field{position:absolute;border:1px solid #8a929c;height:40px;color:var(--white);font-size:11.5px;padding:13px 20px}
.links{left:584px;top:2960px;font-size:12px;line-height:24px;color:var(--white);list-style:none}
.social{position:absolute;top:3113px;width:14px;height:14px;border:1.5px solid var(--muted);border-radius:2px}
.copy{left:584px;top:3193px;font-size:11.5px;line-height:19px;color:var(--white)}
</style>
</head>
<body>

<!-- header -->
<div class="abs brand"><div class="brand-dot"></div><div class="brand-name">MERIDEL<br>BIDDING GROUP</div></div>
<div class="abs call">Call Us. <span>(555) 014-2287</span></div>
<div class="pill" style="left:972px;top:20px;width:168px;height:32px">Get Free Quotes</div>

<nav class="abs nav">
  <svg class="abs" style="left:0;top:0" width="903" height="40" viewBox="0 0 903 40">
    <polygon points="0,40 25,0 166,0 130,40" fill="#acd136"/>
    <polygon points="733,40 773,0 903,0 903,40" fill="#acd136"/>
    <g stroke="#8b929c" stroke-width="1">
      <line x1="260" y1="40" x2="292" y2="0"/>
      <line x1="390" y1="40" x2="422" y2="0"/>
      <line x1="521" y1="40" x2="553" y2="0"/>
    </g>
  </svg>
  <a style="left:65px">HOME</a>
  <a style="left:182px">ABOUT US</a>
  <a style="left:311px">SERVICES</a>
  <a style="left:441px">AUCTIONS</a>
  <a style="left:564px">EQUIPMENT FINDER</a>
  <a style="left:764px">CONTACT US</a>
</nav>

<!-- hero -->
<div class="abs hero" role="img" aria-label="Food packaging machinery on a factory floor, darkened"></div>
<h1 class="abs hero-title">LEADERS IN <b>FOOD MANUFACTURING</b><br>AND <b>PACKAGING EQUIPMENT</b><br>AUCTIONS</h1>
<div class="pill solid" style="left:517px;top:485px;width:167px;height:30px">Equipment Finder</div>
<svg class="abs" style="left:0;top:500px" width="1200" height="150" viewBox="0 0 1200 150">
  <path d="M0,55 C150,-5 300,40 450,115 C560,165 700,150 850,100 C1000,55 1100,35 1200,30 L1200,150 L0,150Z" fill="#acd136"/>
  <path d="M0,62 C150,15 300,55 450,128 C560,165 700,160 850,125 C1000,90 1100,85 1200,92 L1200,150 L0,150Z" fill="#ffffff"/>
</svg>

<!-- welcome -->
<h2 class="abs sec-title" style="top:720px">WELCOME TO<br><span class="hl">MERIDEL</span> BIDDING GROUP</h2>
<div class="abs welcome-media" role="img" aria-label="Collage of workers and industrial food machinery"></div>
<div class="abs welcome-copy">
  <p><b>Meridel Bidding Group</b> is a full-service asset-management company specializing in food manufacturing and packaging equipment. Our goal at Meridel Bidding Group is to provide our customers with a range of options to liquidate their assets. A few of the services we offer are appraisals, asset management, live onsite auctions, online auctions and orderly negotiated sales. We help our customers determine the best options to maximize returns within their given parameters.</p>
  <p>Our experienced staff is committed to providing our customers with satisfaction through hard work, integrity, communication and transparency. It is those characteristics of the people behind Meridel Bidding Group that help make this company a top choice in managing surplus assets for companies of all sizes.</p>
</div>
<div class="pill" style="left:544px;top:1063px;width:168px;height:31px">Discover About Us</div>

<!-- services -->
<section class="abs services" role="img" aria-label="Factory interior backdrop in dark slate"></section>
<h2 class="abs svc-title">OUR <span class="hl">SERVICES</span></h2>
<p class="abs svc-intro">Below are a list of our services please contact us for more information.</p>
<div class="svc-item" style="left:208px;top:1362px"><svg width="16" height="16" viewBox="0 0 16 16"><circle cx="8" cy="8" r="7" fill="none" stroke="#acd136" stroke-width="1.4"/><path d="M4.5,8.2 7,10.5 11.5,5.8" fill="none" stroke="#acd136" stroke-width="1.4"/></svg>Appraisals</div>
<div class="svc-item" style="left:208px;top:1391px"><svg width="16" height="16" viewBox="0 0 16 16"><circle cx="8" cy="8" r="7" fill="none" stroke="#acd136" stroke-width="1.4"/><path d="M4.5,8.2 7,10.5 11.5,5.8" fill="none" stroke="#acd136" stroke-width="1.4"/></svg>Auctions</div>
<div class="svc-item" style="left:208px;top:1420px"><svg width="16" height="16" viewBox="0 0 16 16"><circle cx="8" cy="8" r="7" fill="none" stroke="#acd136" stroke-width="1.4"/><path d="M4.5,8.2 7,10.5 11.5,5.8" fill="none" stroke="#acd136" stroke-width="1.4"/></svg>Real Estate</div>
<div class="svc-item" style="left:381px;top:1362px"><svg width="16" height="16" viewBox="0 0 16 16"><circle cx="8" cy="8" r="7" fill="none" stroke="#acd136" stroke-width="1.4"/><path d="M4.5,8.2 7,10.5 11.5,5.8" fill="none" stroke="#acd136" stroke-width="1.4"/></svg>Asset Management</div>
<div class="svc-item" style="left:381px;top:1391px"><svg width="16" height="16" viewBox="0 0 16 16"><circle cx="8" cy="8" r="7" fill="none" stroke="#acd136" stroke-width="1.4"/><path d="M4.5,8.2 7,10.5 11.5,5.8" fill="none" stroke="#acd136" stroke-width="1.4"/></svg>Orderly Negotiated Sales</div>
<div class="svc-item" style="left:381px;top:1420px"><svg width="16" height="16" viewBox="0 0 16 16"><circle cx="8" cy="8" r="7" fill="none" stroke="#acd136" stroke-width="1.4"/><path d="M4.5,8.2 7,10.5 11.5,5.8" fill="none" stroke="#acd136" stroke-width="1.4"/></svg>Turnkey Operations</div>
<div class="pill" style="left:210px;top:1470px;width:175px;height:31px;color:var(--lime)">Contact Us Today!</div>
<div class="abs svc-media" role="img" aria-label="Collage of processing equipment in green and grey tones"></div>
<svg class="abs" style="left:0;top:1560px" width="1200" height="145" viewBox="0 0 1200 145">
  <path d="M0,50 C150,-5 300,40 450,110 C560,160 700,145 850,95 C1000,50 1100,30 1200,25 L1200,145 L0,145Z" fill="#acd136"/>
  <path d="M0,58 C150,10 300,55 450,122 C560,160 700,155 850,120 C1000,88 1100,82 1200,88 L1200,145 L0,145Z" fill="#ffffff"/>
</svg>

<!-- equipment auctions -->
<h2 class="abs sec-title" style="top:1776px"><span class="hl">EQUIPMENT</span> AUCTIONS</h2>
<svg class="abs" style="left:36px;top:1932px" width="16" height="24" viewBox="0 0 16 24"><path d="M13,2 3,12 13,22" fill="none" stroke="#acd136" stroke-width="2"/></svg>
<svg class="abs" style="left:1148px;top:1932px" width="16" height="24" viewBox="0 0 16 24"><path d="M3,2 13,12 3,22" fill="none" stroke="#acd136" stroke-width="2"/></svg>

<article class="card" style="left:88px">
  <div class="card-img" role="img" aria-label="Blue conveyor lines in a warehouse" style="background:linear-gradient(160deg,#b9bec4,#5a6170 55%,#2f5aa8)"></div>
  <div class="card-date">1/20/2021</div>
  <div class="card-title">Surplus Assets to National Premium Dessert Supplier and Bakery Producer</div>
  <div class="card-loc">Multi Location California &amp; , CO</div>
  <div class="pill">View Details</div>
</article>
<article class="card" style="left:440px">
  <div class="card-img" role="img" aria-label="Long brown belt conveyor in a production hall" style="background:linear-gradient(170deg,#d7d9dc,#8a6a54 50%,#9a9ea3)"></div>
  <div class="card-date">1/7/2021</div>
  <div class="card-title">Large Candy &amp; Confections Surplus Equipment Auction</div>
  <div class="card-loc">Montrose, CO</div>
  <div class="pill">View Details</div>
</article>
<article class="card" style="left:792px">
  <div class="card-img" role="img" aria-label="Stainless steel processing machines" style="background:linear-gradient(160deg,#c9ccd0,#8e9398 55%,#b7babe)"></div>
  <div class="card-date">1/20/2021</div>
  <div class="card-title">Surplus Assets to National Premium Dessert Supplier and Bakery Producer</div>
  <div class="card-loc">Multi Location California &amp; , CO</div>
  <div class="pill">View Details</div>
</article>

<!-- clients -->
<section class="abs clients"></section>
<svg class="abs" style="left:0;top:2290px" width="1200" height="140" viewBox="0 0 1200 140">
  <path d="M0,0 L1200,0 L1200,72 C1050,85 950,5 800,12 C650,20 500,110 300,118 C150,124 50,100 0,92Z" fill="#acd136"/>
  <path d="M0,0 L1200,0 L1200,55 C1050,62 950,0 800,5 C650,12 500,95 300,105 C150,112 50,92 0,82Z" fill="#ffffff"/>
</svg>
<h2 class="abs sec-title" style="top:2388px;color:var(--white)">WHAT OUR <span class="hl">CLIENTS</span> SAY</h2>
<p class="abs quote">“&nbsp;It is a long established fact that a reader will be distracted by the readable content of a page when looking at its layout.&nbsp;”</p>
<div class="abs avatar" role="img" aria-label="Client portrait"></div>
<div class="abs person"><b>Tobias Wrenfield</b><br>Founder</div>
<svg class="abs" style="left:1104px;top:2484px" width="12" height="52" viewBox="0 0 12 52">
  <g fill="none" stroke="#c9ced6" stroke-width="1.2"><circle cx="6" cy="5" r="3.5"/><circle cx="6" cy="19" r="3.5"/><circle cx="6" cy="33" r="3.5"/><circle cx="6" cy="47" r="3.5"/></g>
</svg>

<!-- newsletter -->
<section class="abs newsletter"></section>
<h2 class="abs nl-title">EQUIPMENT EMAIL NOTIFICATION</h2>
<p class="abs nl-sub">Subscribe to get instant notification in your email inbox.</p>
<div class="abs nl-form">
  <svg class="abs" style="left:32px;top:25px" width="24" height="16" viewBox="0 0 24 16"><rect x="1" y="1" width="22" height="14" fill="none" stroke="#acd136" stroke-width="1.4"/><path d="M1,1 12,9 23,1" fill="none" stroke="#acd136" stroke-width="1.4"/></svg>
  <span class="abs" style="left:71px;top:25px;font-size:12px;color:var(--ink)">name@example.com</span>
  <div class="abs nl-btn">SIGN UP</div>
</div>

<!-- footer -->
<footer class="abs footer"></footer>
<h3 class="abs ft-h" style="left:88px;top:2918px">Get Free Quotes</h3>
<div class="field" style="left:88px;top:2962px;width:171px">Your Name</div>
<div class="field" style="left:276px;top:2962px;width:171px">Email</div>
<div class="field" style="left:88px;top:3018px;width:171px">Phone</div>
<div class="field" style="left:276px;top:3018px;width:171px">Subject</div>
<div class="field" style="left:88px;top:3074px;width:359px;height:96px">Message ...</div>
<div class="pill solid" style="left:88px;top:3195px;width:167px;height:37px;border-radius:19px">Send Message</div>

<h3 class="abs ft-h" style="left:584px;top:2918px">Quick Links</h3>
<ul class="abs links">
  <li>Home</li><li>Services</li><li>FAQ's</li><li>Auctions</li><li>Equipment Finder</li><li>Mailing List</li><li>Resources</li><li>Contact Us</li>
</ul>

<h3 class="abs ft-h" style="left:777px;top:2918px">Have any Questions?</h3>
<div class="abs" style="left:777px;top:2952px;font:400 23px 'Barlow Semi Condensed',sans-serif;color:var(--white)">Call Us. (555) 014-2287</div>
<div class="abs" style="left:777px;top:2999px;font-size:11px;color:var(--lime)">CORPORATE OFFICE</div>
<div class="abs" style="left:777px;top:3022px;font-size:11.5px;line-height:24px;color:var(--white)">48 Orchard Line Street Dalworth,<br>ND 50123</div>
<span class="social" style="left:777px"></span>
<span class="social" style="left:805px;border-color:var(--lime)"></span>
<span class="social" style="left:833px"></span>

<div class="abs" style="left:584px;top:3170px;width:527px;height:1px;background:#6b7380"></div>
<svg class="abs" style="left:1133px;top:3162px" width="12" height="16" viewBox="0 0 12 16"><path d="M6,15 V2 M1,7 6,2 11,7" fill="none" stroke="#acd136" stroke-width="1.5"/></svg>
<div class="abs copy">© 2021 Meridel Bidding Group.<br>All Rights Reserved.</div>

</body>
</html>
```